Prepared ready to cook meal delivery service needs a flyer design

We need a flyer design for a startup company based in Cape Town, South Africa. I've attached a few flyer designs that I like.

The company is called 'Brindle' and our website will be found at brindle.co.za. We don't have a logo yet.

Flyer text:

Brindle
Ready to roast

Do you feel like a home cooked meal but don't like shopping, peeling, chopping, cooking, or cleaning up?

We deliver ready to roast free range chicken and fresh vegetables to your door.

To order: SMS your name to 083 614 2958 and we'll call you back.

Only the best ingredients used
Free range chickens. Fresh herbs and vegetables. Virgin olive oil.

No bad carbs!

Ready to roast Free range chicken and fresh veggies
For 2 R99
For 4 R139
Updates

Wording of flyer updated.

Target Market(s)

Local Cape Townians that hate grocery shopping and need help saving time preparing meals.

Industry/Entity Type

Delivery Service

Requirements
Must have
• To find out more: SMS your name to 083 614 2958

```html
<!DOCTYPE html>
<html lang="en">
<head>
<meta charset="utf-8">
<title>Brindle Flyer</title>
<link rel="stylesheet" href="https://fonts.googleapis.com/css2?family=Poppins:wght@700&family=Questrial&display=swap">
<style>
  :root {
    --page-bg: #e9e9e9;
    --flyer-black: #0c0c0c;
    --flyer-charcoal: #1e1e1e;
    --band-grey: #5b5b5b;
    --band-dark: #3c3c3c;
    --text-white: #ffffff;
    --text-soft: #d6d6d6;
    --text-muted: #b5b5b5;
    --oven-dark: #2a2a2a;
    --oven-steel: #777777;
    --roast-gold: #c98a3c;
    --roast-light: #ead6b5;
  }
  * { margin: 0; padding: 0; box-sizing: border-box; }
  html, body {
    width: 1200px; height: 1000px; overflow: hidden;
    background: var(--page-bg);
    font-family: "Questrial", "Century Gothic", sans-serif;
  }
  .flyer {
    position: absolute; left: 80px; top: 140px;
    width: 1040px; height: 720px;
    background: linear-gradient(160deg, var(--flyer-charcoal) 0%, var(--flyer-black) 55%, #050505 100%);
    overflow: hidden;
    color: var(--text-white);
    box-shadow: 0 18px 40px rgba(0,0,0,.25);
  }
  .headline {
    position: absolute; left: 40px; top: 22px; width: 960px;
    font-family: "Poppins", "Century Gothic", sans-serif; font-weight: 700;
    font-size: 58px; line-height: 1; letter-spacing: 1px;
    color: var(--text-soft); text-transform: uppercase;
  }
  .subline {
    position: absolute; left: 40px; top: 88px; width: 960px;
    font-size: 38px; line-height: 1; letter-spacing: 1px;
    color: var(--text-white); text-transform: uppercase;
  }
  .oven-photo {
    position: absolute; left: 40px; top: 144px; width: 450px; height: 400px;
    background: radial-gradient(ellipse at 50% 45%, var(--oven-steel) 0%, var(--oven-dark) 55%, #111 100%);
    border: 2px solid #444;
  }
  .brand {
    position: absolute; left: 40px; top: 290px; width: 450px; text-align: center;
    color: var(--text-white);
  }
  .brand-name { font-size: 78px; line-height: 1; }
  .brand-tagline { font-size: 34px; line-height: 1.1; letter-spacing: 1px; text-transform: uppercase; }
  .roast-photo {
    position: absolute; left: 520px; top: 144px; width: 480px; height: 160px;
    background: radial-gradient(ellipse at 45% 55%, var(--roast-gold) 0%, #8a5a2a 45%, var(--roast-light) 100%);
  }
  .offer {
    position: absolute; left: 520px; top: 318px; width: 480px;
  }
  .offer p { font-size: 16px; line-height: 1.3; color: var(--text-soft); margin-bottom: 6px; }
  .offer .no-carbs {
    font-family: "Poppins", sans-serif; font-weight: 700;
    font-size: 24px; line-height: 1.2; color: var(--text-white); margin: 4px 0 4px;
  }
  .offer .prices {
    font-family: "Poppins", sans-serif; font-weight: 700;
    font-size: 20px; line-height: 1.2; color: var(--text-white); margin-top: 4px;
  }
  .footer-band { position: absolute; left: 0; top: 560px; width: 1040px; height: 160px; }
  .ingredients {
    position: absolute; left: 40px; top: 612px; width: 440px;
    font-size: 17px; line-height: 1.4; color: var(--text-white);
  }
  .order {
    position: absolute; left: 560px; top: 570px; width: 440px; text-align: center;
  }
  .order-icon { display: block; margin: 0 auto 4px; }
  .order-lead, .order-close { font-size: 17px; color: var(--text-soft); line-height: 1.25; }
  .order-number {
    font-family: "Poppins", sans-serif; font-weight: 700;
    font-size: 36px; line-height: 1.15; color: var(--text-white); letter-spacing: 1px;
  }
  .order-web { font-size: 13px; line-height: 1.3; letter-spacing: 4px; color: var(--text-muted); margin-top: 4px; }
</style>
</head>
<body>
  <article class="flyer">
    <h1 class="headline">Don't feel like cooking?</h1>
    <h2 class="subline">But feel like a home cooked roast</h2>

    <svg class="footer-band" width="1040" height="160" viewBox="0 0 1040 160">
      <polygon points="0,0 520,0 540,160 0,160" fill="var(--band-grey)"/>
      <polygon points="520,0 1040,0 1040,160 540,160" fill="var(--band-dark)"/>
    </svg>

    <div class="oven-photo" role="img" aria-label="Photo of an open stainless steel oven"></div>

    <div class="brand">
      <div class="brand-name">Brindle</div>
      <div class="brand-tagline">Ready to roast</div>
    </div>

    <div class="roast-photo" role="img" aria-label="Photo of a golden roast chicken with vegetables"></div>

    <div class="offer">
      <p>Don't feel like shopping, peeling, chopping, cooking, or cleaning up?</p>
      <p>We prepare and deliver ready to roast free range chicken and fresh vegetables to your door.</p>
      <div class="no-carbs">No bad carbs!</div>
      <p>Ready to roast Free range chicken and fresh veggies</p>
      <div class="prices">For 2 R99<br>For 4 R139</div>
    </div>

    <p class="ingredients">Only the best ingredients used Free range chickens.<br>Fresh herbs and vegetables. Virgin olive oil.</p>

    <div class="order">
      <svg class="order-icon" width="30" height="30" viewBox="0 0 36 36" aria-hidden="true">
        <circle cx="18" cy="18" r="16" fill="none" stroke="var(--text-soft)" stroke-width="2"/>
        <path d="M13 10 l3 0 l1.5 5 l-2 1.5 c1 2.5 2.5 4 5 5 l1.5 -2 l5 1.5 l0 3 c-8 1 -15 -6 -14 -14z" fill="var(--text-soft)"/>
      </svg>
      <div class="order-lead">To order SMS your name to</div>
      <div class="order-number">083 614 2958</div>
      <div class="order-close">and we'll call you back.</div>
      <div class="order-web">www.brindle.co.za</div>
    </div>
  </article>
</body>
</html>
```